Steady Harbor Claims Group Business card

Need a business card that stands out that includes name of company,(above) Owners name Moira Lindqvist phone#517-362-4408 email# SteadyHarborCG@mailvane.com and website www.Steadyharborclaimsgroup.net. This is a medical billing company so the card has to relate to that or relate to increasing revenue

```html
<!DOCTYPE html>
<html lang="en">
<head>
<meta charset="utf-8">
<title>Steady Harbor Claims Group – Business Card</title>
<link rel="stylesheet" href="https://fonts.googleapis.com/css2?family=Fira+Sans:wght@600&family=Oxygen:wght@400&display=swap">
<style>
  :root {
    --stage: #4a4a4a;
    --card: #f4f3f2;
    --card-edge: #3d7fd1;
    --ink: #111111;
    --mark: #e24b3b;
  }
  * { margin: 0; padding: 0; box-sizing: border-box; }
  html, body { width: 1200px; height: 1200px; overflow: hidden; }
  body { background: var(--stage); position: relative; font-family: "Oxygen", sans-serif; color: var(--ink); }

  .card {
    position: absolute; left: 148px; width: 902px; height: 542px;
    border: 2px solid var(--card-edge);
    background: var(--card);
  }
  .card--front { top: 38px; }
  .card--back { top: 618px; }

  .card__texture { position: absolute; inset: 0; background: linear-gradient(135deg, #f6f5f4 0%, #efeeed 50%, #f6f5f4 100%); }

  .brand-mark {
    position: absolute; display: flex; align-items: center; gap: 10px;
    transform: translate(-50%, -50%);
    font-family: "Oxygen", sans-serif; font-size: 22px; color: var(--mark); white-space: nowrap;
  }
  .brand-mark__dot { width: 18px; height: 18px; border-radius: 50%; background: var(--mark); }
  .card--front .brand-mark { left: 256px; top: 272px; }
  .card--back .brand-mark { left: 451px; top: 271px; }

  .details { position: absolute; left: 452px; top: 0; }
  .details__company { position: absolute; top: 160px; font-size: 16px; white-space: nowrap; }
  .details__name { position: absolute; top: 182px; font-family: "Fira Sans", sans-serif; font-weight: 600; font-size: 31px; white-space: nowrap; }

  .contact { position: absolute; left: 0; display: flex; align-items: center; white-space: nowrap; }
  .contact__icon { width: 28px; height: 28px; margin-right: 18px; flex: none; }
  .contact--phone { top: 246px; font-size: 26px; }
  .contact--email { top: 285px; font-size: 16px; }
  .contact--web { top: 320px; font-size: 16px; }
</style>
</head>
<body>
  <section class="card card--front">
    <div class="card__texture" role="img" aria-label="Soft pale grey faceted background pattern"></div>
    <div class="brand-mark"><span class="brand-mark__dot"></span>Steady Harbor</div>
    <div class="details">
      <p class="details__company">Steady Harbor CG</p>
      <h1 class="details__name">Moira Lindqvist</h1>
      <p class="contact contact--phone">
        <svg class="contact__icon" viewBox="0 0 28 28" aria-hidden="true"><path d="M9 4c-2 1-3 3-2.5 6 .8 5 4 10 8 13 2 1.5 4 1.5 5.5.5l-2.5-4-2 1c-2-1.5-4-5-4.5-7.5l2-1L11 4z" fill="none" stroke="#111" stroke-width="2" stroke-linejoin="round"/></svg>
        517-362-4408
      </p>
      <p class="contact contact--email">
        <svg class="contact__icon" viewBox="0 0 28 28" aria-hidden="true"><rect x="2" y="6" width="24" height="16" fill="none" stroke="#111" stroke-width="1.4"/><path d="M2 6l12 10L26 6M2 22l9-8M26 22l-9-8" fill="none" stroke="#111" stroke-width="1.4"/></svg>
        SteadyHarborCG@mailvane.com
      </p>
      <p class="contact contact--web">
        <svg class="contact__icon" viewBox="0 0 28 28" aria-hidden="true"><g fill="none" stroke="#111" stroke-width="1.3"><circle cx="14" cy="14" r="12"/><ellipse cx="14" cy="14" rx="5.5" ry="12"/><path d="M14 2v24M2 14h24M4 8h20M4 20h20"/></g></svg>
        www.Steadyharborclaimsgroup.net
      </p>
    </div>
  </section>

  <section class="card card--back">
    <div class="card__texture" role="img" aria-label="Soft pale grey faceted background pattern"></div>
    <div class="brand-mark"><span class="brand-mark__dot"></span>Steady Harbor</div>
  </section>
</body>
</html>
```